Korvanta Business Card

Looking for business card ideas. Company name is Korvanta. Have a few basic ideas on attachment. Please submit anything with the logo and general information from attachment.

Industry/Entity Type

Business

```html
<!DOCTYPE html>
<html lang="en">
<head>
<meta charset="utf-8">
<title>Korvanta Business Card</title>
<link rel="stylesheet" href="https://fonts.googleapis.com/css2?family=Open+Sans:ital,wght@0,400;0,600;0,700;1,700&display=swap">
<style>
  :root {
    --backdrop: #c9c9c9;
    --card-white: #ffffff;
    --card-black: #0e0e0e;
    --card-black-soft: #242424;
    --brand-red: #e3202a;
    --brand-orange: #f47a20;
    --brand-yellow: #ffc20e;
    --ink: #111111;
    --text-light: #ffffff;
  }
  * { box-sizing: border-box; margin: 0; padding: 0; }
  html, body {
    width: 1200px;
    height: 900px;
    overflow: hidden;
    background: var(--backdrop);
    font-family: "Open Sans", Arial, sans-serif;
  }
  .card {
    position: absolute;
    left: 160px;
    top: 170px;
    width: 880px;
    height: 560px;
    border-radius: 38px;
    overflow: hidden;
    background: var(--card-white);
  }
  .card-top {
    position: absolute;
    inset: 0 0 auto 0;
    height: 250px;
    background: var(--card-white);
  }
  .holder-name {
    position: absolute;
    right: 56px;
    top: 44px;
    font-size: 27px;
    font-weight: 600;
    color: var(--ink);
  }
  .brand {
    position: absolute;
    left: 48px;
    top: 100px;
    display: flex;
    align-items: center;
    gap: 22px;
  }
  .brand-dot {
    width: 118px;
    height: 118px;
    border-radius: 50%;
    background: var(--brand-red);
  }
  .brand-name {
    font-size: 82px;
    font-weight: 700;
    color: var(--brand-red);
    line-height: 1;
  }
  .tagline-band {
    position: absolute;
    left: 0;
    right: 0;
    top: 250px;
    height: 34px;
    background: linear-gradient(90deg, var(--brand-red) 0%, var(--brand-red) 25%, var(--brand-orange) 60%, var(--brand-yellow) 100%);
    display: flex;
    align-items: center;
    padding-left: 52px;
  }
  .tagline {
    font-size: 19px;
    font-weight: 700;
    font-style: italic;
    letter-spacing: 0.62em;
    color: var(--ink);
    white-space: nowrap;
  }
  .card-bottom {
    position: absolute;
    left: 0;
    right: 0;
    top: 284px;
    bottom: 0;
    background: radial-gradient(ellipse at 40% 60%, var(--card-black-soft) 0%, var(--card-black) 70%);
  }
  .contact-list {
    position: absolute;
    left: 58px;
    top: 36px;
    list-style: none;
    color: var(--text-light);
    font-size: 25px;
    line-height: 34px;
  }
  .contact-item {
    display: flex;
    align-items: flex-start;
  }
  .contact-icon {
    width: 26px;
    height: 34px;
    margin-right: 12px;
    flex: none;
    fill: var(--brand-red);
  }
  .contact-address {
    display: flex;
    flex-direction: column;
  }
</style>
</head>
<body>
  <main class="card">
    <section class="card-top">
      <p class="holder-name">Dale Moreno, Dir.</p>
      <div class="brand">
        <span class="brand-dot"></span>
        <span class="brand-name">Korvanta</span>
      </div>
    </section>

    <div class="tagline-band">
      <p class="tagline">Leading Churches to the NEXT level</p>
    </div>

    <section class="card-bottom">
      <ul class="contact-list">
        <li class="contact-item">
          <svg class="contact-icon" viewBox="0 0 26 34" aria-hidden="true"><path d="M6 9c2-1 3-1 4 1l2 4c0 1 0 2-1 2l-2 1c1 3 3 5 6 7l1-2c1-1 2-1 3 0l3 2c1 1 1 2 0 3l-2 2c-6 1-15-9-14-16z"/></svg>
          <span>(555) 014-2290</span>
        </li>
        <li class="contact-item">
          <svg class="contact-icon" viewBox="0 0 26 34" aria-hidden="true"><path d="M7 6h12a2 2 0 0 1 2 2v20a2 2 0 0 1-2 2H7a2 2 0 0 1-2-2V8a2 2 0 0 1 2-2zm1 3v9h10V9zm1 12v2h2v-2zm4 0v2h2v-2zm-4 4v2h2v-2zm4 0v2h2v-2z"/></svg>
          <span>(555) 018-3472</span>
        </li>
        <li class="contact-item">
          <svg class="contact-icon" viewBox="0 0 26 34" aria-hidden="true"><path d="M2 11h22v16H2zm2 2v1l9 6 9-6v-1zm0 4v8h18v-8l-9 6z"/></svg>
          <span>dmoreno@korvanta.com</span>
        </li>
        <li class="contact-item">
          <svg class="contact-icon" viewBox="0 0 26 34" aria-hidden="true"><path d="M13 6a11 11 0 1 0 0 22 11 11 0 0 0 0-22zm-1 2.2V12H8.5c.8-2 2-3.4 3.5-3.8zm2 0c1.5.4 2.7 1.8 3.5 3.8H14zM6.6 12a9 9 0 0 1 3-3.2c-.6.9-1.1 2-1.4 3.2zm12.2 0c-.3-1.2-.8-2.3-1.4-3.2a9 9 0 0 1 3 3.2zM4.1 16h3.6c0 .7 0 1.3.1 2H4.1a9 9 0 0 1 0-2zm5.6 0H12v2H9.8zm4.3 0h2.3v2H14zm4.3 0h3.6a9 9 0 0 1 0 2h-3.6zM4.6 20h3.6c.3 1.2.8 2.3 1.4 3.2a9 9 0 0 1-5-3.2zm5.7 0H12v3.8c-.8-.4-1.4-1.6-1.7-3.8zm3.7 0h1.7c-.3 2.2-.9 3.4-1.7 3.8zm3.8 0h3.6a9 9 0 0 1-5 3.2c.6-.9 1.1-2 1.4-3.2z"/></svg>
          <span>www.korvanta.org</span>
        </li>
        <li class="contact-item">
          <svg class="contact-icon" viewBox="0 0 26 34" aria-hidden="true"><path d="M13 7 1 18h4v11h6v-7h4v7h6V18h4z"/></svg>
          <span class="contact-address">
            <span>2408 W. Larkspur Ave.</span>
            <span>Brookhaven, TX 79990</span>
          </span>
        </li>
      </ul>
    </section>
  </main>
</body>
</html>
```